Christmas and New year card

I am looking for a Christmas card to be send in a jpg format. With the following message in English and French <br/><br/>The Acting Chargé d’Affaires of Orvèle Mr Didier Vachon Wishes you a joyful Christmas and a Happy New Year filled with peace and prosperity <br/><br/><br/>Le Chargé d’Affaires a.i Mr Didier Vachon vous souhaite un Joyeux Noel et une heureuse année 2020 remplie de paix, prospérité et santé.

Colors

Designer to choose colors to be used in the design.

```html
<!DOCTYPE html>
<html lang="en">
<head>
<meta charset="utf-8">
<title>Season's Greetings Card</title>
<link rel="stylesheet" href="https://fonts.googleapis.com/css2?family=Cabin+Condensed:wght@600;700&display=swap">
<style>
  :root {
    --snow-light: #f6f8fb;
    --snow-mid: #e3e8ef;
    --snow-shade: #cfd6e0;
    --greeting-red: #d3141f;
    --greeting-navy: #2c2a7a;
    --seal-navy: #1f2a5c;
    --pine-dark: #1f3d2a;
    --pine-mid: #3f6b3c;
    --bauble-red: #b3202a;
    --light-gold: #e9c27a;
  }
  * { margin: 0; padding: 0; box-sizing: border-box; }
  html, body {
    width: 1200px;
    height: 707px;
    overflow: hidden;
    background: var(--snow-light);
  }
  .card {
    position: relative;
    width: 1200px;
    height: 707px;
    overflow: hidden;
    background:
      radial-gradient(ellipse at 20% 30%, var(--snow-light) 0%, transparent 60%),
      radial-gradient(ellipse at 70% 80%, var(--snow-shade) 0%, transparent 55%),
      linear-gradient(160deg, var(--snow-light) 0%, var(--snow-mid) 55%, var(--snow-shade) 100%);
    font-family: "Cabin Condensed", "Arial Narrow", sans-serif;
  }
  .tree-photo {
    position: absolute;
    top: 0;
    right: 0;
    width: 560px;
    height: 707px;
    background:
      radial-gradient(circle at 72% 46%, var(--bauble-red) 0%, transparent 16%),
      radial-gradient(circle at 28% 55%, var(--bauble-red) 0%, transparent 9%),
      radial-gradient(circle at 60% 20%, var(--light-gold) 0%, transparent 14%),
      radial-gradient(circle at 85% 82%, var(--light-gold) 0%, transparent 18%),
      linear-gradient(100deg, rgba(63,107,60,0) 0%, rgba(63,107,60,0.55) 22%, var(--pine-mid) 45%, var(--pine-dark) 100%);
  }
  .greeting {
    position: absolute;
    left: 378px;
    transform: translateX(-50%);
    width: 560px;
    text-align: center;
    text-transform: uppercase;
    font-weight: 700;
    font-size: 32px;
    letter-spacing: 0.5px;
  }
  .greeting-en {
    top: 64px;
    color: var(--greeting-red);
    line-height: 50px;
  }
  .greeting-fr {
    top: 408px;
    color: var(--greeting-navy);
    line-height: 49.5px;
  }
  .mission-seal {
    position: absolute;
    left: 640px;
    top: 67px;
    width: 226px;
    height: 226px;
    border-radius: 50%;
    background: var(--snow-light);
    border: 6px solid var(--seal-navy);
    display: flex;
    align-items: center;
    justify-content: center;
    text-align: center;
  }
  .mission-name {
    font-family: "Cabin Condensed", "Arial Narrow", sans-serif;
    font-weight: 700;
    font-size: 26px;
    line-height: 30px;
    text-transform: uppercase;
    color: var(--greeting-navy);
  }
</style>
</head>
<body>
  <main class="card">
    <div class="tree-photo" role="img" aria-label="Decorated Christmas tree with red baubles, gold ornaments and warm fairy lights"></div>

    <p class="greeting greeting-en">
      The Acting Chargé<br>
      d’Affaires of Orvèle Mr<br>
      Didier Vachon Wishes<br>
      You a Joyful Christmas and<br>
      a Happy New Year Filled<br>
      with Peace and Prosperity
    </p>

    <div class="mission-seal">
      <span class="mission-name">Mission<br>Lumière</span>
    </div>

    <p class="greeting greeting-fr" lang="fr">
      Le Chargé d’Affaires a.i Mr<br>
      Didier Vachon vous souhaite un<br>
      Joyeux Noel et une heureuse<br>
      année 2020 remplie de paix,<br>
      prospérité et santé.
    </p>
  </main>
</body>
</html>
```